Design a Website Mockup / wordpress templete for Ladies Salon

Hello,

I would like to build a website design mockup for a ladies salon.

please be sure to give me a proper customized design. not just a random templete and tell me we can customize for you!!!

i will reject every design will not hold my color or logo.

attached logo .

i would like to have following tab
- call to Action (Book Online)
-Home
- About
- Services & Prices
- Social Link

```html
<!DOCTYPE html>
<html lang="en">
<head>
<meta charset="utf-8">
<title>Lumelle Beauty Center</title>
<link href="https://fonts.googleapis.com/css2?family=Roboto:wght@300;400;500;700&family=Russo+One&display=swap" rel="stylesheet">
<style>
:root{
  --purple:#6a2fc0;
  --purple-dark:#5a22a8;
  --ink:#222;
  --muted:#666;
  --line:#e3e3e3;
  --card:#e2e2e2;
  --dark:#1d1b1b;
  --footer:#050505;
  --footer-bar:#111;
  --white:#fff;
}
*{margin:0;padding:0;box-sizing:border-box}
html,body{width:1200px;height:3395px;overflow:hidden}
body{position:relative;font-family:"Roboto",sans-serif;color:var(--ink);background:var(--white)}
.abs{position:absolute}
.btn{position:absolute;background:var(--purple);color:var(--white);font-size:13px;letter-spacing:1px;display:flex;align-items:center;justify-content:center;text-transform:uppercase}
.btn-dark{background:#000}

/* top bar */
.promo{left:161px;top:60px;font-size:12px;color:#333}
.promo b{color:#000}
.brand{left:450px;top:40px;width:300px;text-align:center;font-family:"Roboto",sans-serif;font-weight:500;font-size:44px;color:var(--purple);display:flex;align-items:center;justify-content:center;gap:12px}
.brand i{display:block;width:22px;height:22px;border-radius:50%;background:var(--purple)}
.brand-sub{left:450px;top:100px;width:300px;text-align:center;font-size:11px;letter-spacing:2px;color:var(--purple)}
.top-rule{left:0;top:125px;width:1200px;height:1px;background:var(--line)}
.nav a{position:absolute;top:140px;font-size:13px;color:#222;text-decoration:none}
.nav a.active{color:var(--purple)}
.nav a.active::before{content:"";position:absolute;left:0;top:-14px;width:38px;height:2px;background:var(--purple)}
.social{display:flex;gap:12px}
.social span{display:block;width:12px;height:12px;border-radius:50%;background:#111}
.social.light span{background:#fff}

/* hero */
.hero{left:0;top:180px;width:1200px;height:427px;background:linear-gradient(90deg,#8a8a8f 0%,#b6b6ba 45%,#e9e2de 70%,#cfc7c4 100%)}
.hero-arc{left:0;top:176px}
.hero-kicker{left:161px;top:335px;font-family:"Russo One",sans-serif;font-size:20px;color:#fff;letter-spacing:2px}
.hero-title{left:161px;top:365px;font-family:"Russo One",sans-serif;font-size:40px;color:#fff;letter-spacing:3px}
.hero-text{left:163px;top:422px;width:430px;font-size:15px;line-height:21px;color:#fff;font-weight:300}
.arrow{position:absolute;width:38px;height:37px;display:flex;align-items:center;justify-content:center}

/* section heads */
.head{position:absolute;left:0;width:1200px;text-align:center;font-size:27px;letter-spacing:3px;color:#111}
.divider{position:absolute;left:478px;width:244px;height:20px}
.divider::before,.divider::after{content:"";position:absolute;top:10px;width:92px;height:1px;background:#777}
.divider::before{left:0}.divider::after{right:0}
.divider i{position:absolute;left:114px;top:3px;width:14px;height:14px;border-radius:50%;background:var(--purple)}

/* services */
.svc{position:absolute;top:760px;width:280px;height:225px;background:var(--card);box-shadow:0 3px 3px rgba(0,0,0,.25);text-align:center}
.svc .ico{position:absolute;left:103px;top:23px;width:74px;height:74px;border-radius:50%;background:var(--purple)}
.svc h3{position:absolute;top:115px;width:100%;font-size:16px;font-weight:500;letter-spacing:2px}
.svc p{position:absolute;top:150px;left:30px;width:220px;font-size:11.5px;line-height:18px;color:#555}

/* about */
.about{left:0;top:1048px;width:1200px;height:437px;background:linear-gradient(90deg,#2a2726,#1a1817 50%,#2b2826)}
.about h2{position:absolute;left:161px;top:1150px;font-size:19px;font-weight:400;letter-spacing:2px;color:#fff}
.about-rule{left:161px;top:1193px;width:246px;height:1px;background:#888}
.about-rule i{position:absolute;left:112px;top:-7px;width:14px;height:14px;border-radius:50%;background:#fff}
.about-text{left:161px;width:418px;font-size:11px;line-height:18px;color:#eee;text-align:justify}
.join{left:693px;top:1100px;width:308px;height:313px;background:#fff}
.join-mark{left:800px;top:1140px;width:94px;height:94px;border-radius:50%;background:#f1ecf8}
.join-text{left:693px;top:1278px;width:308px;text-align:center;font-size:13.5px;line-height:18px;letter-spacing:.5px;color:#222}

/* products */
.prod-img{position:absolute;top:1640px;width:277px;height:307px}
.prod-cap{position:absolute;top:1966px;width:277px;text-align:center;font-size:12.5px;line-height:18px;color:#333}
.prod-price{position:absolute;top:2012px;width:277px;text-align:center;font-size:12.5px;font-style:italic;font-weight:700}

/* testimonial */
.quote-band{left:0;top:2083px;width:1200px;height:322px;background:linear-gradient(90deg,#6426b8,#7a3dc9 55%,#6a2cbf)}
.avatar{left:305px;top:2171px;width:144px;height:144px;border-radius:50%;border:4px solid #fff;background:linear-gradient(135deg,#d9b59b,#a77a64)}
.qmark{left:495px;top:2170px;font-size:56px;font-weight:700;color:#fff;line-height:1;font-family:Georgia,serif}
.quote{left:531px;top:2216px;width:460px;font-size:11.5px;line-height:18px;color:#fff;text-align:justify}
.quote-name{left:531px;top:2310px;font-size:13px;color:#fff}

/* prices */
.plan{position:absolute;top:2557px;width:204px;height:440px;border:1px solid #ddd;background:#fff;text-align:center}
.plan .pic{height:113px}
.plan h3{margin-top:22px;font-size:15px;font-weight:500;letter-spacing:1.5px}
.plan .badge{margin:14px auto 0;width:66px;height:66px;border-radius:50%;background:var(--purple);color:#fff;font-size:16px;font-weight:700;display:flex;align-items:center;justify-content:center}
.plan .badge small{font-size:7px;font-weight:400;margin-left:2px}
.plan ul{list-style:none;margin-top:14px}
.plan li{height:33px;line-height:33px;font-size:11px;color:#666;border-top:1px solid #e8e8e8}
.plan li:first-child{border-top:1px solid #e8e8e8}
.plan .btn{position:absolute;left:37px;top:383px;width:128px;height:32px}

/* footer */
.footer{left:0;top:3061px;width:1200px;height:285px;background:var(--footer)}
.foot-bar{left:0;top:3346px;width:1200px;height:49px;background:var(--footer-bar)}
.foot-brand{left:161px;top:3135px;font-size:32px;font-weight:500;color:#fff;display:flex;align-items:center;gap:10px}
.foot-brand i{display:block;width:18px;height:18px;border-radius:50%;background:#fff}
.foot-about{left:161px;top:3196px;width:220px;font-size:11px;line-height:19px;color:#fff}
.foot-head{top:3123px;font-size:15px;font-weight:500;letter-spacing:1.5px;color:#fff}
.foot-list{list-style:none;font-size:11px;line-height:22px;color:#fff}
.email{left:806px;top:3172px;width:233px;height:33px;background:#fff;font-size:10px;color:#555;padding:11px 11px}
.copy{left:161px;top:3365px;font-size:11px;letter-spacing:1px;color:#fff}
</style>
</head>
<body>

<!-- top bar -->
<div class="abs promo">USE CODE <b>FREESHIP</b> | VALID ON ALL ORDERS!</div>
<div class="abs brand"><i></i>Lumelle</div>
<div class="abs brand-sub">Beauty Center</div>
<div class="btn" style="left:913px;top:52px;width:128px;height:32px;font-size:12px">Online Book</div>
<div class="abs top-rule"></div>
<nav class="nav">
  <a class="active" style="left:161px">HOME</a>
  <a style="left:251px">ABOUT US</a>
  <a style="left:367px">SEVICES</a>
  <a style="left:471px">TESTIMONIALS</a>
  <a style="left:617px">PRICES</a>
  <a style="left:715px">CONTACT US</a>
</nav>
<div class="abs social" style="left:905px;top:142px" aria-label="Social links"><span></span><span></span><span></span><span></span><span></span></div>

<!-- hero -->
<div class="abs hero" role="img" aria-label="Salon photo of a woman with long dark hair touching her face"></div>
<svg class="abs hero-arc" width="1200" height="100" viewBox="0 0 1200 100"><path d="M0 0H1200V100C900 -10 300 -10 0 100Z" fill="#fff"/></svg>
<div class="abs hero-kicker">WELCOME TO</div>
<div class="abs hero-title">LUMELLE BEAUTY CENTER</div>
<p class="abs hero-text">Lorem ipsum dolor sit amet, consectetur adipiscing elit, sed do eiusmod tempor incididunt ut labore et</p>
<div class="btn" style="left:161px;top:486px;width:127px;height:33px">Get Started</div>
<div class="arrow" style="left:0;top:420px;background:var(--purple)"><svg width="10" height="14"><path d="M8 1L2 7l6 6" stroke="#fff" stroke-width="2" fill="none"/></svg></div>
<div class="arrow" style="left:1162px;top:420px;background:#000"><svg width="10" height="14"><path d="M2 1l6 6-6 6" stroke="#fff" stroke-width="2" fill="none"/></svg></div>

<!-- services -->
<h2 class="head" style="top:660px">OUR SERVICES</h2>
<div class="divider" style="top:703px"><i></i></div>
<div class="svc" style="left:161px"><div class="ico"></div><h3>BODY</h3><p>Sed auctor vehicula mi, in vestibulum turpis. Donec non semper odio.</p></div>
<div class="svc" style="left:461px"><div class="ico"></div><h3>MIND</h3><p>Sed auctor vehicula mi, in vestibulum turpis. Donec non semper odio.</p></div>
<div class="svc" style="left:761px"><div class="ico"></div><h3>HEART</h3><p>Sed auctor vehicula mi, in vestibulum turpis. Donec non semper odio.</p></div>

<!-- about -->
<div class="abs about" role="img" aria-label="Dim photo of stylists working in the salon"></div>
<h2 class="about-h" style="position:absolute;left:161px;top:1150px;font-size:19px;font-weight:400;letter-spacing:2px;color:#fff">ABOUT US</h2>
<div class="abs about-rule"><i></i></div>
<p class="abs about-text" style="top:1216px">Lorem ipsum dolor sit amet, consectetur adipiscing elit, sed do eiusmod tempor incididunt ut labore et dolore magna aliqua.</p>
<p class="abs about-text" style="top:1270px">Lorem ipsum dolor sit amet, consectetur adipiscing elit, sed do eiusmod tempor incididunt ut labore et dolore magna aliqua. Ut enim ad minim veniam, quis nostrud exercitation.</p>
<div class="btn" style="left:161px;top:1352px;width:127px;height:33px">Learn More</div>
<div class="abs join"></div>
<div class="abs join-mark"></div>
<p class="abs join-text">Join the other who are enjoying<br>Our Services!</p>
<div class="btn btn-dark" style="left:772px;top:1341px;width:150px;height:31px">Book Online</div>

<!-- products -->
<h2 class="head" style="top:1540px">OUR PRODUCT</h2>
<div class="divider" style="top:1583px"><i></i></div>
<svg class="abs" style="left:120px;top:1790px" width="16" height="30"><path d="M14 1L2 15l12 14" stroke="#111" stroke-width="2" fill="none"/></svg>
<svg class="abs" style="left:1094px;top:1790px" width="16" height="30"><path d="M2 1l12 14L2 29" stroke="#8a5bd0" stroke-width="2" fill="none"/></svg>
<div class="prod-img" style="left:176px;background:#f1e4dd" role="img" aria-label="Bronze tube of foot cream"></div>
<div class="prod-img" style="left:476px;background:#a9a9a9" role="img" aria-label="Black can of volume hair spray"></div>
<div class="prod-img" style="left:776px;background:#e6e6e6" role="img" aria-label="Red tube of hair conditioner"></div>
<p class="prod-cap" style="left:176px">LOREM IPSUM IS SIMPLY DUMMY<br>CONSECTETUR ADIPISCING</p>
<p class="prod-cap" style="left:476px">LOREM IPSUM IS SIMPLY DUMMY<br>CONSECTETUR ADIPISCING</p>
<p class="prod-cap" style="left:776px">LOREM IPSUM IS SIMPLY DUMMY<br>CONSECTETUR ADIPISCING</p>
<p class="prod-price" style="left:176px">$45.00</p>
<p class="prod-price" style="left:476px">$45.00</p>
<p class="prod-price" style="left:776px">$45.00</p>

<!-- testimonial -->
<div class="abs quote-band"></div>
<div class="abs avatar" role="img" aria-label="Portrait of a client having her eye makeup applied"></div>
<div class="abs qmark">&ldquo;</div>
<p class="abs quote">Lorem ipsum dolor sit amet, consectetur adipiscing elit, sed do eiusmod tempor incididunt ut labore et dolore magna aliqua.Lorem ipsum dolor sit amet, consectetur adipiscing elit, sed do eiusmod tempor incididunt ut labore et dolore magna aliqua. Lorem ipsum dolor sit amet, consectetu</p>
<p class="abs quote-name">Roasa Doe</p>

<!-- prices -->
<h2 class="head" style="top:2461px">OUR PRICES</h2>
<div class="divider" style="top:2503px"><i></i></div>
<div class="plan" style="left:161px"><div class="pic" style="background:linear-gradient(135deg,#c9a88c,#e8ddd3)" role="img" aria-label="Stylist blow-drying a client's hair"></div><h3>FAMILY PACK</h3><div class="badge">$70<small>month</small></div><ul><li>Hair Coloring</li><li>Spa Therapy</li><li>Body Massage</li><li>Minicure</li></ul><div class="btn">Buy Now</div></div>
<div class="plan" style="left:381px"><div class="pic" style="background:linear-gradient(135deg,#b88a6e,#efe6df)" role="img" aria-label="Client smiling during a hair styling"></div><h3>MEDIUM</h3><div class="badge">$40<small>month</small></div><ul><li>Body Hand &amp; Foot Message</li><li>Nail Cutting &amp; Styling</li><li>Spa Manicure</li><li>Spa Therapy</li></ul><div class="btn">Buy Now</div></div>
<div class="plan" style="left:610px"><div class="pic" style="background:linear-gradient(135deg,#6b5446,#c9b7a8)" role="img" aria-label="Close-up of hair being blow-dried"></div><h3>PREMIUM</h3><div class="badge">$60<small>month</small></div><ul><li>Hair Coloring</li><li>Spa Therapy with minicure</li><li>Body Hand &amp; Foot Massage</li><li>Manicure</li></ul><div class="btn">Buy Now</div></div>
<div class="plan" style="left:835px"><div class="pic" style="background:linear-gradient(135deg,#5a4038,#d8c2b4)" role="img" aria-label="Group of women laughing at the salon"></div><h3>ULTIMATE</h3><div class="badge">$50<small>month</small></div><ul><li>Nail Cutting &amp; Styling</li><li>Spa Manicure</li><li>Body Massage</li><li>Minicure</li></ul><div class="btn">Buy Now</div></div>

<!-- footer -->
<div class="abs footer"></div>
<div class="abs foot-brand"><i></i>Lumelle</div>
<p class="abs foot-about">Lorem ipsum dolor sit amet, consectetur adipiscing elit. Morbi ac eleifend orci. Nulla facilisi. Nullam dignissim euismod</p>
<div class="abs foot-head" style="left:471px">MENU</div>
<ul class="abs foot-list" style="left:471px;top:3165px"><li>Home</li><li>About us</li><li>Sevices</li><li>Testimonials</li><li>Prices</li><li>Contact us</li></ul>
<div class="abs foot-head" style="left:629px">SERVICES</div>
<ul class="abs foot-list" style="left:629px;top:3165px"><li>Body</li><li>Mind</li><li>Heart</li></ul>
<div class="abs foot-head" style="left:806px">NEWSLETTER</div>
<div class="abs email">Enter Your Email</div>
<div class="btn" style="left:806px;top:3220px;width:127px;height:33px;font-size:12px">Subscribe</div>
<div class="abs foot-bar"></div>
<div class="abs copy">© 2018 Lumelle Beauty Center, LLC. All Rights Reserved</div>
<div class="abs social light" style="left:905px;top:3364px" aria-label="Social links"><span></span><span></span><span></span><span></span><span></span></div>

</body>
</html>
```